Publisher needs book cover for search and rescue book

Book cover needed for book front sized 5.5 x 8.5 inches. About the book: The book is a technical handbook used to instruct either new search and rescue planners involved in the intelligence gathering aspect of a missing person incident or experienced providers who wish to learn new techniques and methods to collect intelligence about a missing person to better plan the field response of where to send resources or identify additional data that needs to be collected. . A background color of navy blue is preferred but open to suggestions. Interested in concepts that suggest collection of intelligence, search and rescue, law enforcement, and should be highly professional in appearance.

Target Market(s)

The target audience for the book is: Search and rescue professionals involved in the collection and analysis of intelligence used to plan where to send resources and law enforcement officers who either look for missing persons or supervise search and rescue resources.

Industry/Entity Type

Search And Rescue

Colors
0455a3

Requirements
Must have
• Title: Quiet Compass
Subtitle: Guiding the Evidence Workflow On the Hunt for Absent Travellers
The author is: Benedict R. Harlow
Image or images that brand the collection of intelligence used in search and rescue/missing persons
Nice to have
• Like the concept of an image of going deeper and deeper which each layer revealing new information.
The author has a concept of a picture that is blurry, one magnify glass reveals what the picture is, a second magnifying glass reveals even greater unexpected finding. Some designers may work with that concept, while I'm open to other designs that synthesize intelligence gathering and search and rescue/law enforcement themes.
Should not have
• No cartoons

```html
<!DOCTYPE html>
<html lang="en">
<head>
<meta charset="utf-8">
<title>Quiet Compass — Front Cover, Design Concept 1</title>
<link rel="stylesheet" href="https://fonts.googleapis.com/css2?family=Michroma&family=Roboto+Condensed:wght@400&family=Montserrat:wght@400&display=swap">
<style>
  :root {
    --board-grey: #58595b;
    --board-label: #e6e6e6;
    --cover-navy: #0a1d6e;
    --cover-navy-deep: #081660;
    --ring-blue: #0f6bb5;
    --ring-blue-soft: #1679c2;
    --title-cyan: #27a6e2;
    --subtitle-white: #ffffff;
    --lens-white: #ffffff;
    --photo-light: #d9d9d9;
    --photo-mid: #9a9a9a;
    --handle-dark: #151515;
    --handle-steel: #b9bcc0;
  }
  * { margin: 0; padding: 0; box-sizing: border-box; }
  html, body {
    width: 840px; height: 1200px; overflow: hidden;
    background: var(--board-grey);
  }
  .board { position: relative; width: 840px; height: 1200px; }
  .board-label {
    position: absolute; left: 0; width: 840px; text-align: center;
    font-family: "Montserrat", sans-serif; font-size: 16px; letter-spacing: 1px;
    color: var(--board-label);
  }
  .board-label--top { top: 54px; }
  .board-label--bottom { top: 1131px; }
  .cover {
    position: absolute; left: 90px; top: 90px; width: 660px; height: 1020px;
    background: linear-gradient(180deg, var(--cover-navy) 0%, var(--cover-navy-deep) 100%);
    overflow: hidden;
    box-shadow: 6px 8px 10px rgba(0,0,0,0.45);
  }
  .cover-art { position: absolute; left: 0; top: 0; width: 660px; height: 680px; }
  .cover-title {
    position: absolute; left: 0; top: 612px; width: 660px; text-align: center;
    font-family: "Michroma", sans-serif; font-weight: 400;
    color: var(--title-cyan); text-transform: uppercase;
    font-size: 60px; line-height: 78px; letter-spacing: 4px;
    text-shadow: 2px 3px 4px rgba(0,0,0,0.45);
  }
  .cover-subtitle {
    position: absolute; left: 0; top: 778px; width: 660px; text-align: center;
    font-family: "Roboto Condensed", sans-serif; font-weight: 400;
    color: var(--subtitle-white); font-size: 28px; line-height: 38px;
  }
  .cover-author {
    position: absolute; left: 0; top: 912px; width: 660px; text-align: center;
    font-family: "Michroma", sans-serif; color: var(--title-cyan);
    font-size: 22px; letter-spacing: 2px; text-transform: uppercase;
  }
</style>
</head>
<body>
  <div class="board">
    <p class="board-label board-label--top">Front Cover</p>

    <div class="cover">
      <svg class="cover-art" viewBox="0 0 660 680" xmlns="http://www.w3.org/2000/svg">
        <defs>
          <radialGradient id="portrait-tone" cx="50%" cy="45%" r="55%">
            <stop offset="0%" stop-color="var(--photo-light)"/>
            <stop offset="100%" stop-color="var(--photo-mid)"/>
          </radialGradient>
          <linearGradient id="handle-tone" x1="0" y1="0" x2="1" y2="0">
            <stop offset="0%" stop-color="var(--handle-steel)"/>
            <stop offset="25%" stop-color="var(--handle-steel)"/>
            <stop offset="30%" stop-color="var(--handle-dark)"/>
            <stop offset="100%" stop-color="var(--handle-dark)"/>
          </linearGradient>
        </defs>

        <g class="search-halo">
          <circle cx="332" cy="348" r="222" fill="var(--ring-blue)" opacity="0.9"/>
          <circle cx="332" cy="348" r="200" fill="none" stroke="var(--ring-blue-soft)" stroke-width="1.2" opacity="0.8"/>
          <circle cx="332" cy="348" r="190" fill="none" stroke="#8fb8dd" stroke-width="0.8" opacity="0.6"/>
        </g>

        <circle class="lens-ring" cx="332" cy="348" r="173" fill="var(--lens-white)"/>

        <circle class="portrait-placeholder" cx="332" cy="350" r="154" fill="url(#portrait-tone)"
                role="img" aria-label="Blurred black and white photograph of a missing person seen through a magnifying glass lens"/>

        <rect class="handle-placeholder" x="0" y="-18" width="210" height="36" rx="6"
              fill="url(#handle-tone)" transform="translate(480 408) rotate(33)"
              role="img" aria-label="Handle of a magnifying glass"/>
      </svg>

      <h1 class="cover-title">Quiet<br>Compass</h1>
      <p class="cover-subtitle">Guiding the Evidence Workflow<br>On the Hunt for Absent Travellers</p>
      <p class="cover-author">Benedict R. Harlow</p>
    </div>

    <p class="board-label board-label--bottom">Design Concept 1</p>
  </div>
</body>
</html>
```